Tallivo Limited Business Card

We need a business card for a new company based in Essex, United Kingdom. We develop and manufacture educational games. The business card needs to match the company brand and logo and the colour scheme.
My company makes educational board games to be played by the family or used by teachers
The games are tile based number game

Target Market(s)

Parents, teachers, schools and children

Industry/Entity Type

Games

Contact Information for Business Card

Company Name - Tallivo Limited
Director - Martin Dobbs
Registered Office - 3 Birch Court, 241 Harwell Lane, Marlow Vale, Hartshire, HV4 4TP
Phone Number - 07841 563 218
Email - Enquiries@Tallivo.example
Website - www.Tallivo.example
Company Number - 08471362

Font styles to use
Sans Serif

Colors
00a990
ffffff

Requirements
Must have
• Same colour scheme as the attachments - green and white
• Same font style for Tallivo
• Images of the number tiles similar to the attachments
• extra details
• The colour is Cyan - 82 Magenta - 24 Yellow - 44 Black - 2
• I have attached some of the font styles use on my website and alos my LOGO
Nice to have
• Image of the number "1" tag as seen on the website

```html
<!DOCTYPE html>
<html lang="en">
<head>
<meta charset="utf-8">
<title>Tallivo Limited – Business Card</title>
<link href="https://fonts.googleapis.com/css2?family=Open+Sans:wght@400;600&family=Nunito:wght@800&display=swap" rel="stylesheet">
<style>
  :root {
    --teal: #1b9696;
    --green: #17a98f;
    --white: #ffffff;
    --backdrop: #3b3631;
    --text-teal: #1a8f8f;
  }
  * { margin: 0; padding: 0; box-sizing: border-box; }
  html, body { width: 1200px; height: 930px; overflow: hidden; }
  body {
    background: var(--backdrop);
    font-family: "Open Sans", sans-serif;
    position: relative;
  }
  .card {
    position: absolute;
    left: 250px;
    width: 700px;
    height: 400px;
    border-radius: 18px;
    overflow: hidden;
  }
  .card-front { top: 40px; background: var(--teal); }
  .card-back { top: 490px; background: var(--white); }

  .brand-name {
    font-family: "Nunito", sans-serif;
    font-weight: 800;
    line-height: 1;
    letter-spacing: -1px;
  }
  .tagline {
    font-weight: 400;
    text-transform: uppercase;
    letter-spacing: 0.5px;
  }

  .front-brand {
    position: absolute;
    left: 0; right: 0; top: 130px;
    text-align: center;
    color: var(--white);
  }
  .front-brand .brand-name { font-size: 92px; }
  .front-brand .tagline { font-size: 21px; margin-top: 4px; }

  .back-brand {
    position: absolute;
    left: 48px; top: 42px;
    color: var(--text-teal);
  }
  .back-brand .brand-name { font-size: 66px; }
  .back-brand .tagline { font-size: 16px; margin-top: 2px; }
  .company-number { font-size: 15px; margin-top: 4px; letter-spacing: 0.3px; }

  .person {
    position: absolute;
    right: 48px; top: 178px;
    text-align: right;
    color: var(--text-teal);
  }
  .person-name { font-size: 26px; font-weight: 600; line-height: 1; text-transform: uppercase; }
  .person-role { font-size: 15px; margin-top: 4px; }
  .divider {
    position: absolute;
    left: 48px; right: 48px; top: 238px;
    height: 1.5px;
    background: var(--text-teal);
  }
  .address {
    position: absolute;
    right: 48px; top: 250px;
    text-align: right;
    color: var(--text-teal);
    font-size: 15px;
    font-style: normal;
    line-height: 1.45;
  }
  .contacts {
    position: absolute;
    left: 48px; top: 262px;
    list-style: none;
    color: var(--text-teal);
    font-size: 16px;
    line-height: 1.55;
  }
  .contacts li { display: flex; align-items: center; gap: 12px; }
  .contacts svg { width: 13px; height: 13px; flex: none; }

  .corner-bands { position: absolute; left: 0; bottom: 0; width: 700px; height: 110px; }
</style>
</head>
<body>

  <section class="card card-front" aria-label="Card front">
    <div class="front-brand">
      <div class="brand-name">Tallivo</div>
      <div class="tagline">Quick-fire counting games</div>
    </div>
  </section>

  <section class="card card-back" aria-label="Card back">
    <div class="back-brand">
      <div class="brand-name">Tallivo</div>
      <div class="tagline">Quick-fire counting games</div>
      <div class="company-number">Company Number - 08471362</div>
    </div>

    <div class="person">
      <div class="person-name">Martin Dobbs</div>
      <div class="person-role">Director</div>
    </div>
    <div class="divider"></div>
    <address class="address">
      3 Birch Court, 241 Harwell Lane,<br>
      Marlow Vale, Hartshire, HV4 4TP
    </address>

    <ul class="contacts">
      <li>
        <svg viewBox="0 0 16 16" aria-hidden="true"><path d="M4 1l3 3-2 2c1 2 3 4 5 5l2-2 3 3-2 2C7 14 2 9 2 3z" fill="var(--text-teal)"/></svg>
        07841 563 218
      </li>
      <li>
        <svg viewBox="0 0 16 16" aria-hidden="true"><rect x="1.5" y="3.5" width="13" height="9" fill="none" stroke="var(--text-teal)" stroke-width="1.5"/><path d="M1.5 3.5l6.5 5 6.5-5" fill="none" stroke="var(--text-teal)" stroke-width="1.5"/></svg>
        Enquiries@Tallivo.example
      </li>
      <li>
        <svg viewBox="0 0 16 16" aria-hidden="true"><circle cx="8" cy="8" r="6.5" fill="none" stroke="var(--text-teal)" stroke-width="1.4"/><ellipse cx="8" cy="8" rx="2.8" ry="6.5" fill="none" stroke="var(--text-teal)" stroke-width="1.2"/><path d="M1.5 8h13" stroke="var(--text-teal)" stroke-width="1.2"/></svg>
        www.Tallivo.example
      </li>
    </ul>

    <svg class="corner-bands" viewBox="0 0 700 110" aria-hidden="true">
      <polygon points="0,98 420,60 420,110 0,110" fill="var(--green)"/>
      <polygon points="432,58 440,20 700,20 700,110 424,110" fill="var(--teal)"/>
    </svg>
  </section>

</body>
</html>
```